Create Design/GRAPHICS/TEXT FOR KORVEL/E-COMMERCE PRODUCT

Hi,
I am looking for a designer to create a advertisement/images/text for a product that I sell on Korvel.
The first attachment is a 3d rendering of the product that I sell and want to use as the main image of the design.
The second attachment is of a existing ad on Korvel that you can use as a general idea of how I want the final graphic to look like.
The third and fourth attachments are of the text/graphics that I would like for you to include in the graphic.
Finally, the last attachment is my logo that I would like to include in the graphic.
Please feel free to get creative with this and if you have any questions please feel free to contact me.-
Update-I just added source files for logo as attachment six.
Thanks!
KORVEL
Product

```html
<!DOCTYPE html>
<html lang="en">
<head>
<meta charset="utf-8">
<title>HALDEN BBQ Access Doors</title>
<link href="https://fonts.googleapis.com/css2?family=Open+Sans:ital,wght@0,400;0,600;0,700;0,800;1,400&family=Cinzel:wght@500&display=swap" rel="stylesheet">
<style>
  :root{
    --ink:#111;
    --paper:#fff;
    --accent:#2a8fd6;
    --steel-light:#e4e5e6;
    --steel-dark:#9a9c9e;
  }
  *{margin:0;padding:0;box-sizing:border-box}
  html,body{width:1200px;height:854px;overflow:hidden;background:var(--paper)}
  body{position:relative;font-family:"Open Sans",sans-serif;color:var(--ink)}
  .brand{position:absolute;left:78px;top:44px;font-family:"Cinzel",serif;font-weight:500;font-size:50px;letter-spacing:1px;color:var(--ink)}
  .product-render{position:absolute;left:50px;top:115px;width:580px;height:475px;
    background:radial-gradient(ellipse at 50% 45%,var(--steel-light) 0%,#c9cbcd 55%,var(--paper) 80%)}
  .headline{position:absolute;right:60px;top:18px;text-align:right}
  .headline h1{font-weight:600;font-size:32px;line-height:44px;padding-bottom:4px;border-bottom:2.5px solid var(--ink);padding-left:2px}
  .headline p{font-style:italic;font-size:24px;margin-top:4px;padding-right:2px}
  .features{position:absolute;left:663px;top:188px;list-style:none;font-size:18px;line-height:22px}
  .features li{margin-bottom:22px}
  .features li.sub{margin-bottom:0}
  .features li.group-start{margin-bottom:0}
  .features li.group-end{margin-bottom:22px}
  .features li::before{content:"• "}
  .features li.first::before{color:var(--accent)}
  .features li.sub::before{content:"· "}
  .badges{position:absolute;left:61px;top:598px;display:flex;gap:25px}
  .badge{width:125px;height:224px;border:2px solid var(--ink);display:flex;flex-direction:column}
  .badge-art{height:124px;display:flex;align-items:center;justify-content:center}
  .badge-label{height:26px;border-top:2px solid var(--ink);border-bottom:2px solid var(--ink);font-size:12px;text-align:center;line-height:22px;font-weight:600}
  .badge-note{flex:1;background:var(--ink);color:var(--paper);font-size:11px;font-weight:600;text-align:center;line-height:14px;padding-top:17px}
</style>
</head>
<body>
  <div class="brand">HALDEN</div>

  <div class="product-render" role="img" aria-label="3D render of an open stainless steel BBQ access door with a paper towel holder on the inside of the door"></div>

  <header class="headline">
    <h1>Hand Crafted BBQ Acess Doors</h1>
    <p>Elegant Design with Durable Construction</p>
  </header>

  <ul class="features">
    <li class="first"><b>Premium grade</b>&nbsp; T-304 Stainless Steel Construction</li>
    <li><b>Rugged</b> 16 gauge square frame construction</li>
    <li class="group-start"><b>DOUBLE WALL</b> Construction</li>
    <li class="sub">19 gauge outer wall</li>
    <li class="sub group-end">20 gauge inner wall</li>
    <li><b>Secure</b> 4 point magnectic closing system</li>
    <li><b>High Quality</b> T-304 grade Stainless Steelhandles</li>
    <li><b>Convenient</b> paper towel holder</li>
  </ul>

  <section class="badges">
    <div class="badge">
      <div class="badge-art">
        <svg width="110" height="110" viewBox="0 0 110 110">
          <defs><path id="arcTop1" d="M22 55 A33 33 0 0 1 88 55"/><path id="arcBot1" d="M30 66 A27 27 0 0 0 80 66"/></defs>
          <circle cx="55" cy="55" r="42" fill="none" stroke="#111" stroke-width="2.5"/>
          <text font-size="8" font-family="Open Sans,sans-serif"><textPath href="#arcTop1" startOffset="50%" text-anchor="middle">HANDCRAFTED</textPath></text>
          <rect x="10" y="45" width="90" height="20" fill="#111"/>
          <text x="55" y="59" fill="#fff" font-size="11" font-weight="700" text-anchor="middle" font-family="Open Sans,sans-serif">HANDCRAFTED</text>
          <text font-size="7" font-family="Open Sans,sans-serif"><textPath href="#arcBot1" startOffset="50%" text-anchor="middle">with pride</textPath></text>
        </svg>
      </div>
      <div class="badge-label">QUALITY</div>
      <div class="badge-note">Our employes take<br>pride in their work</div>
    </div>

    <div class="badge">
      <div class="badge-art">
        <svg width="110" height="110" viewBox="0 0 110 110">
          <line x1="5" y1="28" x2="105" y2="28" stroke="#111" stroke-width="2"/>
          <line x1="5" y1="33" x2="105" y2="33" stroke="#111" stroke-width="2"/>
          <text x="55" y="58" font-size="12.5" font-weight="700" text-anchor="middle" font-family="Open Sans,sans-serif">DOUBLE WALL</text>
          <text x="55" y="74" font-size="12.5" font-weight="700" text-anchor="middle" font-family="Open Sans,sans-serif">CONSTRUCTION</text>
          <line x1="5" y1="88" x2="105" y2="88" stroke="#111" stroke-width="2"/>
          <line x1="5" y1="93" x2="105" y2="93" stroke="#111" stroke-width="2"/>
        </svg>
      </div>
      <div class="badge-label">VALUE</div>
      <div class="badge-note" style="padding-top:10px">Our doors weight<br>10 pounds more than<br>the competition</div>
    </div>

    <div class="badge">
      <div class="badge-art">
        <svg width="120" height="120" viewBox="0 0 120 120">
          <text x="60" y="17" font-size="11.5" font-weight="600" text-anchor="middle" font-family="Open Sans,sans-serif">PREMIUM GRADE</text>
          <line x1="10" y1="24" x2="110" y2="24" stroke="#111" stroke-width="3"/>
          <text x="60" y="62" font-size="36" font-weight="800" text-anchor="middle" font-family="Open Sans,sans-serif">T-304</text>
          <text x="60" y="82" font-size="10.5" font-weight="600" text-anchor="middle" font-family="Open Sans,sans-serif">STRAINLESS STEEL</text>
          <line x1="10" y1="93" x2="110" y2="93" stroke="#111" stroke-width="3"/>
        </svg>
      </div>
      <div class="badge-label">STRENGHT</div>
      <div class="badge-note">Offers higher level of<br>corrosion resistance</div>
    </div>

    <div class="badge">
      <div class="badge-art">
        <svg width="120" height="120" viewBox="0 0 120 120">
          <text x="60" y="30" font-size="34" font-weight="800" text-anchor="middle" font-family="Open Sans,sans-serif">16G</text>
          <line x1="28" y1="36" x2="92" y2="36" stroke="#111" stroke-width="3"/>
          <text x="60" y="49" font-size="9" font-weight="600" text-anchor="middle" font-family="Open Sans,sans-serif">FRAME</text>
          <text x="60" y="86" font-size="34" font-weight="800" text-anchor="middle" font-family="Open Sans,sans-serif">18G</text>
          <line x1="28" y1="92" x2="92" y2="92" stroke="#111" stroke-width="3"/>
          <text x="60" y="106" font-size="9" font-weight="600" text-anchor="middle" font-family="Open Sans,sans-serif">OUTER WALL</text>
        </svg>
      </div>
      <div class="badge-label">DURABILITY</div>
      <div class="badge-note" style="padding-top:10px">Thick and Durable<br>Stainless Steel<br>construction</div>
    </div>

    <div class="badge">
      <div class="badge-art">
        <svg width="110" height="110" viewBox="0 0 110 110">
          <defs><path id="arcTop5" d="M22 55 A33 33 0 0 1 88 55"/><path id="arcBot5" d="M30 66 A27 27 0 0 0 80 66"/></defs>
          <circle cx="55" cy="55" r="42" fill="none" stroke="#111" stroke-width="2.5"/>
          <text font-size="8" font-family="Open Sans,sans-serif"><textPath href="#arcTop5" startOffset="50%" text-anchor="middle">SATISFACTION</textPath></text>
          <rect x="10" y="44" width="90" height="22" fill="#111"/>
          <text x="55" y="61" fill="#fff" font-size="16" font-weight="700" text-anchor="middle" font-family="Open Sans,sans-serif">100%</text>
          <text font-size="7" font-family="Open Sans,sans-serif"><textPath href="#arcBot5" startOffset="50%" text-anchor="middle">Guaranteed</textPath></text>
        </svg>
      </div>
      <div class="badge-label">PEACE OF MIND</div>
      <div class="badge-note">Your satisfaction is<br>our highest goal</div>
    </div>
  </section>
</body>
</html>
```